Logo for a recruitment consultancy and executive search firm
The Ashcombe Reeve Partnership
Logo for a recruitment consultancy and executive search firm - Consulting
Creative Brief
Professional
Marian Colbeck
Head of Practice
London office: Belgrove Court 42 Belgrove Court Mayfair London W1K 4PL Dublin office: Block C The Larchfield House Oakpark, Kilbarrow Dublin, 9
marian@ashcombe-reeve.example
www.ashcombe-reeve.example
We will need 3 other business cards details are as follows: Name: Tarek Haddadi Title: Head of Practice Address: London office: Belgrove Court 42 Belgrove Court Mayfair London W1K 4PL Dublin office: Block C The Larchfield House Oakpark, Kilbarrow Dublin, 9 Phone: 020 7946 0321 Mobile: 07700900482 Email: tarek@ashcombe-reeve.example Name: Judith Purcell Title: CEO Address: London office: Belgrove Court 42 Belgrove Court Mayfair London W1K 4PL Dublin office: Block C The Larchfield House Oakpark, Kilbarrow Dublin, 9 Phone: 020 7946 0321 Mobile: 07700 900 615 Email: judith@ashcombe-reeve.example Name: Helen Varty Title: Finance Manager Address: London office: Belgrove Court 42 Belgrove Court Mayfair London W1K 4PL Dublin office: Block C The Larchfield House Oakpark, Kilbarrow Dublin, 9 0321 Mobile: 07700 900 738 email: accounts@ashcombe-reeve.example We want the complete stationary set! The more the merrier as far as I am concerned. folders compliment strips headed paper email signature envelopes presentation format position documents folder you name it we want it!
Black with Ashcombe reeve logo

```html
<!DOCTYPE html>
<html lang="en">
<head>
<meta charset="utf-8">
<title>The Ashcombe Reeve Partnership – Business Cards</title>
<link rel="stylesheet" href="https://fonts.googleapis.com/css2?family=Cinzel:wght@400&family=Cormorant+Garamond:wght@500&display=swap">
<style>
  :root {
    --page: #e4e4e4;
    --card: #2a2624;
    --ink-light: #f4f2ef;
    --ink-muted: #c9c4bf;
    --band-white: #f7f7f7;
    --band-silver-1: #d9d9d9;
    --band-silver-2: #9a9a9a;
    --band-text: #3a3634;
  }
  * { box-sizing: border-box; margin: 0; padding: 0; }
  html, body { width: 1200px; height: 984px; overflow: hidden; }
  body {
    background: var(--page);
    position: relative;
    font-family: "Cormorant Garamond", Georgia, serif;
  }
  .card {
    position: absolute;
    left: 280px;
    width: 640px;
    height: 366px;
    background: var(--card);
    border-radius: 18px;
    overflow: hidden;
    box-shadow: 0 10px 24px rgba(0,0,0,0.22);
    color: var(--ink-light);
  }
  .card--back { top: 96px; }
  .card--front { top: 522px; }

  /* Brand name set as plain text */
  .brand-name {
    font-family: "Cormorant Garamond", Georgia, serif;
    font-weight: 500;
    color: var(--ink-light);
    white-space: nowrap;
  }

  /* Back */
  .back-brand {
    position: absolute;
    top: 156px; left: 0; right: 0;
    text-align: center;
    font-size: 26px;
    letter-spacing: 1px;
  }
  .back-web {
    position: absolute;
    top: 204px; left: 0; right: 0;
    text-align: center;
    font-family: "Cinzel", serif;
    font-size: 10px;
    letter-spacing: 5px;
    color: var(--ink-muted);
    text-transform: uppercase;
  }

  /* Front */
  .front-brand {
    position: absolute;
    top: 96px; left: 34px;
    font-size: 22px;
    letter-spacing: 0.5px;
  }
  .contact-list {
    position: absolute;
    top: 148px; left: 34px;
    list-style: none;
    font-size: 11.5px;
    line-height: 15px;
    color: var(--ink-muted);
  }
  .contact-list li { display: flex; align-items: flex-start; gap: 8px; margin-bottom: 2px; }
  .contact-icon { flex: none; width: 12px; height: 12px; margin-top: 1px; }
  .person {
    position: absolute;
    right: 36px; top: 256px;
    text-align: right;
    font-family: "Cinzel", serif;
  }
  .person-name { font-size: 15px; letter-spacing: 1px; }
  .person-role { font-size: 10px; letter-spacing: 1.5px; color: var(--ink-muted); margin-top: 2px; }
  .band { position: absolute; left: 0; bottom: 0; width: 640px; height: 62px; }
  .band-web {
    position: absolute;
    right: 40px; bottom: 16px;
    font-family: "Cinzel", serif;
    font-size: 11px;
    letter-spacing: 3px;
    color: var(--band-text);
    text-transform: uppercase;
  }
</style>
</head>
<body>

<section class="card card--back" aria-label="Business card, reverse">
  <div class="brand-name back-brand">The Ashcombe Reeve Partnership</div>
  <div class="back-web">www.ashcombe-reeve.example</div>
</section>

<section class="card card--front" aria-label="Business card, front">
  <div class="brand-name front-brand">The Ashcombe Reeve Partnership</div>

  <ul class="contact-list">
    <li>
      <svg class="contact-icon" viewBox="0 0 12 12"><circle cx="6" cy="6" r="6" fill="#c9c4bf"/><path d="M6 2.5a2.2 2.2 0 0 0-2.2 2.2C3.8 6.4 6 9.5 6 9.5s2.2-3.1 2.2-4.8A2.2 2.2 0 0 0 6 2.5z" fill="#2a2624"/></svg>
      <span>Block C The Larchfield House<br>Oakpark, Kilbarrow Dublin, 9</span>
    </li>
    <li>
      <svg class="contact-icon" viewBox="0 0 12 12"><circle cx="6" cy="6" r="6" fill="#c9c4bf"/><path d="M3.6 3.2l1.3-.3.7 1.6-.8.6a4 4 0 0 0 2 2l.6-.8 1.6.7-.3 1.3C6 8.5 3.4 6 3.6 3.2z" fill="#2a2624"/></svg>
      <span>020 7946 0321</span>
    </li>
    <li>
      <svg class="contact-icon" viewBox="0 0 12 12"><circle cx="6" cy="6" r="6" fill="#c9c4bf"/><rect x="3" y="3.8" width="6" height="4.4" rx="0.5" fill="#2a2624"/><path d="M3.2 4l2.8 2.2L8.8 4" fill="none" stroke="#c9c4bf" stroke-width="0.6"/></svg>
      <span>marian@ashcombe-reeve.example</span>
    </li>
    <li>
      <svg class="contact-icon" viewBox="0 0 12 12"><circle cx="6" cy="6" r="6" fill="#c9c4bf"/><circle cx="6" cy="6" r="3" fill="none" stroke="#2a2624" stroke-width="0.9"/><path d="M3 6h6M6 3v6" stroke="#2a2624" stroke-width="0.7"/></svg>
      <span>www.ashcombe-reeve.example</span>
    </li>
  </ul>

  <div class="person">
    <div class="person-name">Marian Colbeck</div>
    <div class="person-role">Head of Practice</div>
  </div>

  <svg class="band" viewBox="0 0 640 62" aria-hidden="true">
    <defs>
      <linearGradient id="silver" x1="0" y1="0" x2="1" y2="0">
        <stop offset="0" stop-color="#9a9a9a"/>
        <stop offset="0.5" stop-color="#d9d9d9"/>
        <stop offset="1" stop-color="#9a9a9a"/>
      </linearGradient>
    </defs>
    <path d="M0 30 H250 Q262 30 266 22 Q270 12 284 12 H640 V62 H0 Z" fill="url(#silver)"/>
    <path d="M0 36 H254 Q266 36 270 28 Q274 18 288 18 H640 V62 H0 Z" fill="#f7f7f7"/>
    <path d="M0 36 H254 Q266 36 270 28 Q274 18 288 18 H640" fill="none" stroke="#bdbdbd" stroke-width="1"/>
  </svg>
  <div class="band-web">www.ashcombe-reeve.example</div>
</section>

</body>
</html>
```